Financial Services Business Card Design

We are a financial services company Based in London, offering Short term Funding Solutions for companies, raising anywhere between £20,000 and £25million pounds.

The Card must have a professional look as it is going to be handed out to professionals I.E Solicitors, Accountants, Company directors and Business owners.

See Attached our company Logo

Industry/Entity Type

Business

Contact Information for Business Card

Lewis Thorncroft
Suite 41
R K House
Bramblecote Lane
Elmsworth
HP19 4QX

```html
<!DOCTYPE html>
<html lang="en">
<head>
<meta charset="utf-8">
<title>Quillmere Bridging – Business Card</title>
<link rel="stylesheet" href="https://fonts.googleapis.com/css2?family=Lato:wght@300;400;700;900&display=swap">
<style>
  :root {
    --backdrop: #e6e7e9;
    --card-white: #ffffff;
    --card-dark-top: #1c1c1c;
    --card-dark-bottom: #0d0d0d;
    --curve-shadow: #b9babd;
    --brand-blue: #1b6fbd;
    --text-dark: #262626;
    --text-light: #ffffff;
  }
  * { margin: 0; padding: 0; box-sizing: border-box; }
  html, body {
    width: 1200px;
    height: 920px;
    overflow: hidden;
    background: var(--backdrop);
    font-family: "Lato", sans-serif;
  }
  .stage {
    position: relative;
    width: 1200px;
    height: 920px;
  }
  .card {
    position: absolute;
    top: 337px;
    width: 460px;
    height: 294px;
    overflow: hidden;
    box-shadow: 0 2px 6px rgba(0,0,0,0.18);
  }
  .card-front { left: 106px; }
  .card-back { left: 639px; }
  .card-shapes {
    position: absolute;
    inset: 0;
    display: block;
  }
  .brand-name {
    position: absolute;
    left: 0;
    right: 0;
    text-align: center;
    font-weight: 900;
    font-size: 28px;
    letter-spacing: 0.3px;
    color: var(--brand-blue);
    line-height: 1;
    white-space: nowrap;
  }
  .card-front .brand-name { top: 121px; }
  .card-back .brand-name { top: 213px; }
  .holder-name {
    position: absolute;
    left: 0;
    right: 0;
    top: 233px;
    text-align: center;
    font-size: 20px;
    font-weight: 400;
    line-height: 24px;
    color: var(--text-light);
  }
  .address {
    position: absolute;
    left: 0;
    right: 0;
    top: 21px;
    text-align: center;
    font-size: 14.5px;
    font-weight: 300;
    line-height: 19px;
    color: var(--text-dark);
    font-style: normal;
    white-space: nowrap;
  }
</style>
</head>
<body>
<main class="stage">

  <section class="card card-front">
    <svg class="card-shapes" viewBox="0 0 460 294" aria-hidden="true">
      <defs>
        <linearGradient id="darkFill" x1="0" y1="0" x2="0" y2="1">
          <stop offset="0" stop-color="var(--card-dark-top)"/>
          <stop offset="1" stop-color="var(--card-dark-bottom)"/>
        </linearGradient>
      </defs>
      <rect width="460" height="294" fill="url(#darkFill)"/>
      <path d="M0 0 H460 V113 Q230 299 0 113 Z" fill="var(--curve-shadow)"/>
      <path d="M0 0 H460 V113 Q230 275 0 113 Z" fill="var(--card-white)"/>
    </svg>
    <div class="brand-name">Quillmere Bridging</div>
    <p class="holder-name">Lewis Thorncroft</p>
  </section>

  <section class="card card-back">
    <svg class="card-shapes" viewBox="0 0 460 294" aria-hidden="true">
      <defs>
        <linearGradient id="darkFillBack" x1="0" y1="0" x2="0" y2="1">
          <stop offset="0" stop-color="var(--card-dark-top)"/>
          <stop offset="1" stop-color="var(--card-dark-bottom)"/>
        </linearGradient>
      </defs>
      <rect width="460" height="294" fill="url(#darkFillBack)"/>
      <path d="M0 0 H460 Q230 190 0 0 Z" fill="var(--curve-shadow)"/>
      <path d="M0 0 H460 Q230 162 0 0 Z" fill="var(--card-white)"/>
    </svg>
    <address class="address">
      Suite 41,&nbsp; R K House,&nbsp; Bramblecote Lane<br>
      Elmsworth,&nbsp; HP19 4QX
    </address>
    <div class="brand-name">Quillmere Bridging</div>
  </section>

</main>
</body>
</html>
```